Vastmere Holdings Webpage Design

We need a new website for our company. The company is Vastmere Holdings Pty Ltd. We are in the business of Asbestos Removal; Demolition; Earthworks and Transport. We do not advertise and would like our website to be a reference point for our clients / potential clients and also to make our services known to those searching the internet for the services we offer. Some examples of the style of website we are after are:
http://www.quorrintdemolition.com.au/
http://m.feltrovindemolitions.com.au/
http://www.pinsettodemolition.com.au
http://www.rulqa.com.au
http://www.tjhservices.com.au
http://www.steadfield-deconstruction.com.au
We will need to work on content. Enclosed is an example. We also need to purchase the domain vastmereholdings.com.au and need to set up email accounts and ensure the website is mobile friendly. We have a company logo and have built our business on delivering professional, quality services on time. We would like the webpage to be simple, informative and professional - black and white / grey themed. We would also like to add a photo gallery etc later.

Industry/Entity Type

Construction

Coding

Coded - Design and coding required

Number of Pages Required

1 page

Colors
000000
fcfcfc
959595
dddddd

Requirements
Must have
• Information regarding the services we provide

```html
<!DOCTYPE html>
<html lang="en">
<head>
<meta charset="utf-8">
<title>Vastmere Holdings – Demolition &amp; Earthworks</title>
<link href="https://fonts.googleapis.com/css2?family=Open+Sans:wght@400;600;700&family=Raleway:wght@600;700&family=Roboto:wght@400;500&display=swap" rel="stylesheet">
<style>
:root{
  --accent:#a9bfca;
  --accent-dark:#93aab6;
  --page:#f2f2f2;
  --panel:#ececec;
  --ink:#333333;
  --muted:#8f8f8f;
  --line:#dddddd;
  --white:#fcfcfc;
  --footer:#2e3338;
}
*{box-sizing:border-box;margin:0;padding:0}
html,body{width:1200px;height:3536px;overflow:hidden}
body{position:relative;background:var(--page);font-family:"Open Sans",Arial,sans-serif;color:var(--ink)}
.abs{position:absolute}
.photo{position:absolute}

/* Hero */
.hero{left:0;top:0;width:1200px;height:700px;background:linear-gradient(180deg,#b9cfd6 0%,#a6c0ca 70%,#c9dbe1 100%)}
.hero-machine{left:170px;top:30px;width:870px;height:660px;background:radial-gradient(ellipse at 60% 60%,rgba(60,64,66,.55),rgba(60,64,66,0) 65%)}
.brand{left:85px;top:38px;font-family:"Roboto",Arial,sans-serif;font-size:30px;font-weight:400;letter-spacing:4px;color:#3a3d40}
.nav{right:70px;top:40px;display:flex;gap:26px;font-size:13px;color:#2d3033}
.hero-title{left:349px;top:330px;font-family:"Raleway",Arial,sans-serif;font-weight:700;font-size:66px;letter-spacing:6px;color:#f4f6f7}
.hero-text{left:351px;top:410px;width:340px;font-size:15px;line-height:21px;letter-spacing:1px;text-transform:uppercase;color:#2f3336}
.btn-dark{left:351px;top:511px;width:142px;height:36px;background:#2d3033;color:var(--white);font-size:14px;letter-spacing:1.5px;display:flex;align-items:center;justify-content:center}

/* Shared headings */
.section-title{font-family:"Roboto",Arial,sans-serif;font-size:19px;letter-spacing:4px;color:#3a3d40;text-align:center}
.rule{height:2px;width:40px;background:#8c9aa2}
.lead{font-size:13px;line-height:22px;color:var(--muted);text-align:center}

/* About */
.about-title{left:151px;top:795px;font-family:"Roboto",Arial,sans-serif;font-size:19px;letter-spacing:4px;color:#3a3d40}
.about-text{left:151px;top:862px;width:370px;font-size:13px;line-height:22px;color:var(--muted)}
.btn-light{background:var(--accent);color:var(--white);font-size:14px;letter-spacing:2px;display:flex;align-items:center;justify-content:center}
.about-btn{left:148px;top:1032px;width:142px;height:38px}
.about-photo{left:625px;top:799px;width:389px;height:269px;background:linear-gradient(180deg,#6fa3d8 0%,#9cc1e0 40%,#a58465 75%,#7b5c43 100%)}

/* Services */
.service{position:absolute;width:462px;height:205px;background:#f5f5f5;border:1px solid #e4e4e4}
.service.is-active{background:var(--accent);border-color:var(--accent)}
.service .icon{position:absolute;left:28px;top:28px;width:94px;height:94px;border-radius:50%;background:var(--accent)}
.service.is-active .icon{background:var(--white)}
.service h3{position:absolute;left:148px;top:40px;font-size:13px;font-weight:600;letter-spacing:.5px;color:#8a8a8a}
.service.is-active h3{color:var(--white)}
.service .bar{position:absolute;left:148px;top:72px;width:40px;height:1px;background:#cfcfcf}
.service.is-active .bar{background:var(--white)}
.service p{position:absolute;left:148px;top:92px;width:290px;font-size:12.5px;line-height:22px;color:#9a9a9a}
.service.is-active p{color:var(--white)}

/* Earthworks */
.earthworks{left:0;top:1893px;width:1200px;height:386px;background:linear-gradient(180deg,#5f6569 0%,#6c7276 55%,#5a5f62 100%)}
.earth-title{left:0;top:1944px;width:1200px;font-family:"Roboto",Arial,sans-serif;font-weight:500;font-size:20px;letter-spacing:4px;color:var(--white);text-align:center}
.earth-text{left:300px;top:2014px;width:600px;font-size:13px;font-weight:600;line-height:20px;color:var(--white);text-align:center}
.earth-item{position:absolute;top:2090px;width:220px;text-align:center}
.earth-item .glyph{width:70px;height:62px;margin:0 auto;border-radius:4px;background:rgba(252,252,252,.85)}
.earth-item span{display:block;margin-top:24px;font-size:13.5px;font-weight:700;color:var(--white)}

/* Projects */
.projects{left:0;top:2282px;width:1200px;height:247px;background:var(--panel)}
.project{top:2529px;width:400px;height:281px}
.project-1{left:0;background:linear-gradient(180deg,#3d86d8 0%,#8fb7de 45%,#9c8f80 75%,#6f665d 100%)}
.project-2{left:400px;background:linear-gradient(180deg,#6d8296 0%,#8d9aa6 50%,#9a9486 100%)}
.project-3{left:800px;background:linear-gradient(180deg,#2f7fd6 0%,#8fb7dc 45%,#8b7c65 75%,#5d4e3d 100%)}
.project-overlay{left:412px;top:2548px;width:370px;height:262px;background:rgba(190,214,222,.72)}
.view-btn{left:542px;top:2648px;width:118px;height:36px;border:1px solid var(--white);background:rgba(255,255,255,.25);color:var(--white);font-size:12px;letter-spacing:1px;display:flex;align-items:center;justify-content:center}

/* Contact */
.field{position:absolute;background:#ebebeb;border:1px solid #e2e2e2;font-size:13px;color:#a5a5a5;padding:12px 14px}
.contact-item{position:absolute;left:750px;display:flex;align-items:flex-start;gap:26px;font-size:13px;line-height:20px;color:#8a8a8a}
.contact-item svg{flex:none}

.footer{left:0;top:3460px;width:1200px;height:76px;background:var(--footer);color:var(--white);font-size:13.5px;font-weight:600;display:flex;align-items:center;justify-content:center}
</style>
</head>
<body>

<!-- Hero -->
<section class="abs hero" role="img" aria-label="Photo of an orange and grey tracked excavator with a demolition grapple attachment on a pale blue backdrop"></section>
<div class="photo hero-machine" aria-hidden="true"></div>
<div class="abs brand">VASTMERE HOLDINGS</div>
<nav class="abs nav">
  <span>Home</span><span>Services</span><span>Gallery</span><span>Demolition Costs</span><span>About</span><span>Quote</span><span>Contact</span>
</nav>
<h1 class="abs hero-title">DEMOLITION</h1>
<p class="abs hero-text">We provide professional demolition services to numerous commercial clients on both large and small skale projects</p>
<div class="abs btn-dark">GET STARTED</div>

<!-- About -->
<h2 class="abs about-title">ABOUT US</h2>
<p class="abs about-text">Vastmere Transport Pty Ltd was established by Director Dorian Vastmere in 2002 with a focus providing services within the transport industry. Over time the company has developed and expanded to include the provision of Earthworks and Demolition.</p>
<div class="abs btn-light about-btn">READ MORE</div>
<div class="photo about-photo" role="img" aria-label="Photo of a yellow excavator loading a dump truck under a blue sky"></div>

<!-- Demolition services -->
<h2 class="abs section-title" style="left:0;top:1192px;width:1200px">DEMOLITION</h2>
<div class="abs rule" style="left:580px;top:1232px"></div>
<p class="abs lead" style="left:295px;top:1260px;width:610px">Vastmere Transport and Demolition provide an extensive range of demolition services. A large amount of experience across a broad range of projects results in a dependable service and peace of mind for all clients.</p>

<article class="service is-active" style="left:123px;top:1360px">
  <div class="icon" role="img" aria-label="Commercial demolition machine icon"></div>
  <h3>COMMERCIAL DEMOLITION</h3><div class="bar"></div>
  <p>Lorem Ipsum is simply dummy text thprinting andthe industry's standard dummy text lorem ipsum is simply dummy</p>
</article>
<article class="service" style="left:615px;top:1360px">
  <div class="icon" role="img" aria-label="Infrastructure demolition machine icon"></div>
  <h3>INFRASTRUCTURE DEMOLITION</h3><div class="bar"></div>
  <p>Lorem Ipsum is simply dummy text thprinting andthe industry's standard dummy text lorem ipsum is simply dummy</p>
</article>
<article class="service" style="left:123px;top:1600px">
  <div class="icon" role="img" aria-label="Domestic demolition machine icon"></div>
  <h3>DOMESTIC DEMOLITION</h3><div class="bar"></div>
  <p>Lorem Ipsum is simply dummy text thprinting andthe industry's standard dummy text lorem ipsum is simply dummy</p>
</article>
<article class="service" style="left:615px;top:1600px">
  <div class="icon" role="img" aria-label="Partial demolition and strip out machine icon"></div>
  <h3>PARTIAL DEMOLITION / STRIP OUT</h3><div class="bar"></div>
  <p>Lorem Ipsum is simply dummy text thprinting andthe industry's standard dummy text lorem ipsum is simply dummy</p>
</article>

<!-- Earthworks -->
<section class="abs earthworks" role="img" aria-label="Darkened photo of an excavator on rubble in front of city towers"></section>
<h2 class="abs earth-title">EARTHWORKS</h2>
<div class="abs rule" style="left:580px;top:1982px;background:var(--white)"></div>
<p class="abs earth-text">Vastmere Transport and Demolition possess all necessary equipment and skilled personnel to provide earthmoving services including:</p>
<div class="earth-item" style="left:156px"><div class="glyph" role="img" aria-label="Excavator icon"></div><span>DEEP EXCAVATION</span></div>
<div class="earth-item" style="left:385px"><div class="glyph" role="img" aria-label="Bricks and hammer icon"></div><span>BULK EARTHWORKS</span></div>
<div class="earth-item" style="left:611px"><div class="glyph" role="img" aria-label="Trees icon"></div><span>TREE REMOVAL</span></div>
<div class="earth-item" style="left:835px"><div class="glyph" role="img" aria-label="Jackhammer icon"></div><span>BULK EARTHWORKS</span></div>

<!-- Projects -->
<section class="abs projects"></section>
<h2 class="abs section-title" style="left:0;top:2354px;width:1200px">OUR PROJECTS</h2>
<div class="abs rule" style="left:580px;top:2394px"></div>
<p class="abs lead" style="left:330px;top:2432px;width:540px">Lorem Ipsum is simply dummy text of the printing and typesetting industry been the industry's standard dummy text</p>
<div class="photo project project-1" role="img" aria-label="Photo of an excavator demolishing a building into rubble"></div>
<div class="photo project project-2" role="img" aria-label="Photo of a yellow excavator clearing a collapsed house"></div>
<div class="photo project project-3" role="img" aria-label="Photo of an excavator working beside power infrastructure"></div>
<div class="abs project-overlay"></div>
<div class="abs view-btn">VIEW DEATIL</div>

<!-- Contact -->
<h2 class="abs section-title" style="left:0;top:2878px;width:1200px">CONTACT US</h2>
<div class="abs rule" style="left:580px;top:2918px"></div>
<p class="abs lead" style="left:330px;top:2955px;width:540px">Lorem Ipsum is simply dummy text of the printing and typesetting industry been the industry's standard dummy text</p>

<div class="field" style="left:186px;top:3064px;width:236px;height:43px">Your Name</div>
<div class="field" style="left:453px;top:3064px;width:233px;height:43px">Email Address</div>
<div class="field" style="left:186px;top:3130px;width:500px;height:193px">Message</div>
<div class="abs btn-light" style="left:186px;top:3347px;width:142px;height:38px">SEND</div>

<div class="contact-item" style="top:3116px">
  <svg width="20" height="28" viewBox="0 0 20 28" aria-hidden="true"><path d="M10 0C4.5 0 0 4.4 0 9.8 0 17 10 28 10 28s10-11 10-18.2C20 4.4 15.5 0 10 0zm0 13.5a3.7 3.7 0 1 1 0-7.4 3.7 3.7 0 0 1 0 7.4z" fill="#a9bfca"/></svg>
  <span>PO Box 482 Kelvendale<br>QLD 4391</span>
</div>
<div class="contact-item" style="top:3188px">
  <svg width="22" height="16" viewBox="0 0 22 16" aria-hidden="true"><rect x="1" y="1" width="20" height="14" fill="none" stroke="#a9bfca" stroke-width="1.6"/><path d="M1 1l10 8 10-8" fill="none" stroke="#a9bfca" stroke-width="1.6"/></svg>
  <span>office@vastmereholdings.com.au</span>
</div>
<div class="contact-item" style="top:3242px">
  <svg width="20" height="20" viewBox="0 0 20 20" aria-hidden="true"><path d="M4 1l3.5 4-2 2.5c1.2 2.7 3.3 4.8 6 6L14 11.5l4 3.5-2 3.5C8.5 18 2 11.5 1.5 4z" fill="#a9bfca"/></svg>
  <span>+0491 570 118</span>
</div>

<footer class="abs footer">Vastmere Holdings Pty Ltd. All Rights Reserved</footer>

</body>
</html>
```